New Label Design Project Velora Hair Care Product Line

The brand name is Velora Hair Care. I would like the designs to stand out and that it will compliment cobalt blue jars and bottles (4oz and 8oz). I would like for the designs to be elegant, attractive, eye catching with a goddess feel to it (the name Velora is Greek) and have enough to list product information on them. I have attached the product details to be put on the labels. I hope this helps. I appreciate your time.
Doreen Whitcombe

Target Market(s)

Hair and Beauty industry

Industry/Entity Type

Hair Care Product

Colors
33a6d7
faa54b
acd037

Requirements
Must have
• Brand colors are Blue, green, and orange, must be able to fit label sizes indicated in the attachment
Nice to have
• creative graphic designs :)

```html
<!DOCTYPE html>
<html lang="en">
<head>
<meta charset="utf-8">
<title>Velora Hair Care – Luminara Moisturizing Mint Shampoo Label</title>
<link href="https://fonts.googleapis.com/css2?family=Marcellus&family=Lato:wght@400;700&display=swap" rel="stylesheet">
<style>
  :root {
    --backdrop: #e4e3e0;
    --navy: #1b2f8c;
    --white: #ffffff;
  }
  html, body {
    margin: 0;
    width: 1200px;
    height: 1200px;
    overflow: hidden;
    background: var(--backdrop);
  }
  .label {
    position: absolute;
    left: 160px;
    top: 62px;
    width: 880px;
    height: 1077px;
    box-shadow: 0 4px 14px rgba(0,0,0,0.18);
  }
  .label svg { display: block; width: 100%; height: 100%; }
  .brand-name { font-family: "Marcellus", serif; fill: var(--white); }
  .product-title { font-family: "Marcellus", serif; fill: var(--white); font-size: 92px; }
  .product-subtitle { font-family: "Lato", sans-serif; fill: var(--white); font-size: 21px; letter-spacing: 5px; }
  .tagline { font-family: "Lato", sans-serif; fill: var(--navy); font-size: 18px; }
  .size-mark { font-family: "Lato", sans-serif; fill: var(--navy); font-size: 19px; }
  .info-text { font-family: "Lato", sans-serif; fill: var(--white); font-size: 13.6px; }
  .info-head { font-weight: 700; }
</style>
</head>
<body>
<div class="label">
  <svg viewBox="0 0 706 864" xmlns="http://www.w3.org/2000/svg">
    <defs>
      <linearGradient id="goldSheen" x1="0" y1="0" x2="1" y2="0">
        <stop offset="0" stop-color="#a17d45"/>
        <stop offset="0.3" stop-color="#d9ac5a"/>
        <stop offset="0.55" stop-color="#fbcd66"/>
        <stop offset="0.85" stop-color="#f8c862"/>
        <stop offset="1" stop-color="#a8834d"/>
      </linearGradient>
      <linearGradient id="navyBand" x1="0" y1="0" x2="1" y2="0">
        <stop offset="0" stop-color="#16207a"/>
        <stop offset="1" stop-color="#1b4fb0"/>
      </linearGradient>
      <radialGradient id="figureGlow" cx="0.45" cy="0.4" r="0.6">
        <stop offset="0" stop-color="#fbf3dc" stop-opacity="0.7"/>
        <stop offset="0.6" stop-color="#fbf3dc" stop-opacity="0.3"/>
        <stop offset="1" stop-color="#fbf3dc" stop-opacity="0"/>
      </radialGradient>
      <radialGradient id="swirlGlow" cx="0.5" cy="0.5" r="0.5">
        <stop offset="0" stop-color="#ffffff" stop-opacity="0.45"/>
        <stop offset="1" stop-color="#ffffff" stop-opacity="0"/>
      </radialGradient>
    </defs>

    <!-- label ground -->
    <rect class="label-ground" width="706" height="864" fill="url(#goldSheen)"/>
    <rect class="label-frame" x="14" y="14" width="678" height="836" fill="none" stroke="#ffffff" stroke-width="1.5"/>

    <!-- goddess silhouette area -->
    <rect class="goddess-figure" role="img" aria-label="Pale cream silhouette of a Greek goddess with flowing hair and a raised hand" x="0" y="20" width="420" height="640" fill="url(#figureGlow)"/>

    <!-- brand name -->
    <text class="brand-name" x="655" y="160" text-anchor="end" font-size="58">Velora</text>
    <text class="brand-name" x="655" y="215" text-anchor="end" font-size="32">HAIR CARE</text>

    <!-- product title -->
    <text class="product-title" x="348" y="400" text-anchor="middle" textLength="620" lengthAdjust="spacingAndGlyphs">LUMINARA</text>
    <text class="product-subtitle" x="662" y="442" text-anchor="end">MOISTURIZING MINT SHAMPOO</text>

    <text class="tagline" text-anchor="end">
      <tspan x="664" y="497">A natural approach to healthy hair</tspan>
      <tspan x="664" y="524">care designed for chemically treated</tspan>
      <tspan x="664" y="551">and non chemically treated hair.</tspan>
    </text>
    <text class="size-mark" x="664" y="600" text-anchor="end">8oz</text>

    <!-- wave bands -->
    <path class="white-swoosh" d="M0 605 C120 560 230 565 320 600 C420 640 560 700 706 690 L706 864 L0 864 Z" fill="#ffffff"/>
    <path class="navy-band" d="M0 643 C110 620 230 625 330 660 C430 695 570 720 706 700 L706 864 L0 864 Z" fill="url(#navyBand)"/>

    <!-- swirl ornament area -->
    <circle class="swirl-ornament" role="img" aria-label="White spiral swirl ornament" cx="525" cy="635" r="62" fill="url(#swirlGlow)"/>

    <!-- butterfly accents -->
    <circle class="butterfly-accent" role="img" aria-label="Small white butterfly" cx="68" cy="540" r="14" fill="#ffffff" fill-opacity="0.85"/>
    <circle class="butterfly-accent" role="img" aria-label="White butterfly" cx="142" cy="672" r="22" fill="#ffffff"/>
    <circle class="butterfly-accent" role="img" aria-label="White butterfly" cx="350" cy="695" r="26" fill="#ffffff"/>

    <!-- product information -->
    <text class="info-text">
      <tspan x="42" y="737"><tspan class="info-head">Description:</tspan> Cleansing shampoo that will</tspan>
      <tspan x="42" y="752">leave hair moisturized without stripping</tspan>
      <tspan x="42" y="767">the hair.  Infused with peppermint to leave</tspan>
      <tspan x="42" y="782">the scalp feeling refreshed.</tspan>
      <tspan x="42" y="800"><tspan class="info-head">Directions:</tspan> Wet hair.  Shake bottle prior to</tspan>
      <tspan x="42" y="815">use, ingredients may tend to settle. Apply</tspan>
      <tspan x="42" y="830">to hair. Lather and rinse.  Repeat. Follow up</tspan>
      <tspan x="42" y="845">with Solenne Conditioner.</tspan>
    </text>
    <text class="info-text" text-anchor="end">
      <tspan x="664" y="755"><tspan class="info-head">Ingredients:</tspan> Organic Aloe Juice, Organic</tspan>
      <tspan x="664" y="769">Soybean Oil, Safflower Oil, Avocado Oil, Palm</tspan>
      <tspan x="664" y="783">Oil, Sunflower Oil, Organic Coconut Oil,</tspan>
      <tspan x="664" y="797">Organic Hemp Seed Oil, Shea Butter, Organic</tspan>
      <tspan x="664" y="811">Cocoa Butter, Organic Olive Oil, Organic Dark</tspan>
      <tspan x="664" y="825">Chocolate Extract, Organic Peppermint Oil,</tspan>
      <tspan x="664" y="839">Menthol, Vitamin E, Rosemary Extract, Citric Acid</tspan>
    </text>
  </svg>
</div>
</body>
</html>
```